Satchel & Compass needs new business card design

I need a new business card design. I'm looking for out-of-the-box design which represents the freedom of being a location independent entrepreneur.
I offer coaching, retreats and trips.
I would like to see designs with and without the photo.
Colors I use are black (#000000), green (#25A796) and brown (#D7C38C)
Website satchelandcompass.com

Target Market(s)

location independent entrepreneurs, digital nomads, people looking to swap the 9 to 5 for a lifestyle business

Industry/Entity Type

Business

Contact Information for Business Card

Petra Varga
Your Lifestyle Business Coach, Retreat & Trip Leader
http://satchelandcompass.com
hello@satchelandcompass.com
Live a life you don't need a holiday from

Font styles to use
Serif
Sans Serif

Requirements
Must have
• One side should contain only the logo. I would also consider having the "Live a life you don't need a holiday from" on that side too (depending on how it looks)
• Please show both sides on the designs.

```html
<!DOCTYPE html>
<html lang="en">
<head>
<meta charset="utf-8">
<title>Satchel &amp; Compass – Business Card</title>
<link rel="stylesheet" href="https://fonts.googleapis.com/css2?family=Nunito:wght@700;800&family=Josefin+Sans:wght@700&display=swap">
<style>
  :root {
    --ink: #000000;
    --ink-soft: #1c1c1c;
    --green: #25A796;
    --green-light: #3bb8a6;
    --brown: #D7C38C;
    --brown-light: #e4d6a8;
    --white: #ffffff;
    --stage: #2b2b2b;
  }
  * { margin: 0; padding: 0; box-sizing: border-box; }
  html, body {
    width: 1200px; height: 900px; overflow: hidden;
    background: var(--stage);
  }
  .canvas { position: relative; width: 1200px; height: 900px; }

  .card {
    position: absolute;
    width: 665px; height: 380px;
    border-radius: 26px;
    overflow: hidden;
  }

  /* Front: logo side */
  .card--front {
    left: 150px; top: 50px;
    background: linear-gradient(135deg, var(--brown-light) 0%, var(--brown) 60%, #cdb77c 100%);
  }
  .brand-name {
    position: absolute; left: 0; right: 0; top: 120px;
    text-align: center;
    font-family: "Nunito", sans-serif;
    font-weight: 800;
    font-size: 58px;
    color: var(--ink-soft);
    letter-spacing: 1px;
  }
  .tagline {
    position: absolute; right: 70px; bottom: 62px;
    font-family: "Nunito", sans-serif;
    font-weight: 700;
    font-size: 22px;
    color: var(--ink);
  }

  /* Back: contact side */
  .card--back {
    left: 385px; top: 470px;
    background: var(--green);
  }
  .portrait {
    position: absolute; left: 0; top: 0;
    width: 440px; height: 100%;
    background:
      radial-gradient(ellipse at 40% 55%, #d9dccf 0%, rgba(217,220,207,0) 35%),
      linear-gradient(160deg, #8a9a6a 0%, #5f6e45 40%, #9aa27a 70%, #6d7b4d 100%);
    -webkit-mask-image: linear-gradient(90deg, #000 55%, transparent 100%);
            mask-image: linear-gradient(90deg, #000 55%, transparent 100%);
  }
  .contact {
    position: absolute; right: 40px; top: 55px;
    text-align: right;
    color: var(--white);
  }
  .person-name {
    font-family: "Josefin Sans", sans-serif;
    font-weight: 700;
    font-size: 38px;
    letter-spacing: 7px;
    color: var(--brown);
    line-height: 1;
  }
  .person-role {
    margin-top: 6px;
    font-family: "Nunito", sans-serif;
    font-weight: 700;
    font-size: 14px;
  }
  .contact-list {
    list-style: none;
    margin-top: 70px;
    font-family: "Nunito", sans-serif;
    font-weight: 700;
    font-size: 18px;
    line-height: 1.7;
  }
  .contact-list li { display: flex; justify-content: flex-end; align-items: center; gap: 10px; }
  .contact-icon { width: 16px; height: 16px; flex: none; }
</style>
</head>
<body>
<main class="canvas">
  <section class="card card--front">
    <p class="brand-name">Satchel &amp; Compass</p>
    <p class="tagline">Live a life you don't need a holiday from</p>
  </section>

  <section class="card card--back">
    <div class="portrait" role="img" aria-label="Photo of the coach sitting on a wooden fence among trees, holding a small sign"></div>
    <div class="contact">
      <h1 class="person-name">PETRA VARGA</h1>
      <p class="person-role">Your Lifestyle Business Coach, Retreat &amp; Trip Leader</p>
      <ul class="contact-list">
        <li>hello@satchelandcompass.com
          <svg class="contact-icon" viewBox="0 0 16 16" aria-hidden="true"><path d="M1 8 L15 2 L11 14 L8 9 Z" fill="#D7C38C"/></svg>
        </li>
        <li>www.satchelandcompass.com
          <svg class="contact-icon" viewBox="0 0 16 16" aria-hidden="true"><circle cx="8" cy="8" r="6.5" fill="none" stroke="#D7C38C" stroke-width="1.6"/><path d="M1.5 8h13M8 1.5c-3 3.5-3 9.5 0 13M8 1.5c3 3.5 3 9.5 0 13" fill="none" stroke="#D7C38C" stroke-width="1.2"/></svg>
        </li>
      </ul>
    </div>
  </section>
</main>
</body>
</html>
```